Wordpress Design Project

Need a new website designed for a spin off company we own. We are a On-Site temporary housing Company specializing in rental Mobile homes, Travel trailers, and Park Models. Our clients are homeowners who are looking to do major remodeling jobs on their homes and need to move out of their home for the remodel. We bring in one of our temporary units for them to live in on their site as they remodel. WE also help people who are looking to do new home construction, and want to live on their site as they are building. This Company called " Brightmoor Dwelling Co" is a spin off of our Flagship company called Cobalt Portable Lodging (www.cobaltlodging.example) this company rents to people who have a need for on-site housing after a house fire or other disaster. Cobalt rents to Insurance company's who have a insured with a loss ( B2B). Brightmoor Dwelling Co will rent home owners directly ( B2C). We will provide you with photos for a Gallery page, and Videolinks for a video page.

Target Market(s)

people looking to rent a temporary home while they are building a home or remodeling a home

Industry/Entity Type

House

Requirements
Must have
• open - but must have a few photos that I will submit that help tell the story of hat we do.
Nice to have
• links to video we will provide -youtube vids

```html
<!DOCTYPE html>
<html lang="en">
<head>
<meta charset="utf-8">
<title>Brightmoor Dwelling Co – On-Site Temporary Housing</title>
<link href="https://fonts.googleapis.com/css2?family=Arimo:wght@400;700&display=swap" rel="stylesheet">
<style>
:root{
  --red:#e8262b;
  --ink:#222;
  --text:#555;
  --muted:#888;
  --nav:#e9e9e9;
  --line:#dcdcdc;
  --navy:#1d3d6e;
  --bg:#fff;
}
*{box-sizing:border-box;margin:0;padding:0}
html,body{width:839px;height:1200px;overflow:hidden;background:var(--bg)}
body{position:relative;font-family:"Arimo",Arial,sans-serif;color:var(--text);font-size:9px;line-height:1.45}
.abs{position:absolute}
/* header */
.brand{left:78px;top:14px;display:flex;align-items:center;gap:8px}
.brand-mark{width:26px;height:26px;background:var(--red)}
.brand-name{font-size:24px;font-weight:700;color:var(--navy);line-height:1.05;width:250px;text-transform:uppercase}
.phone{right:78px;top:12px;font-size:26px;font-weight:700;color:var(--ink);line-height:1}
.email{right:78px;top:44px;font-size:9.5px;color:var(--text)}
.search{left:414px;top:92px;width:131px;height:18px;border:1px solid var(--line);font-size:8px;color:var(--muted);padding:3px 6px}
.search svg{position:absolute;right:5px;top:4px}
.quote{left:573px;top:80px;width:188px;height:32px;border:1px solid var(--line);background:#f7f7f7;display:flex;align-items:center;gap:10px;padding-left:16px;font-size:15px;font-weight:700;color:var(--ink)}
.quote i{width:18px;height:18px;background:var(--red);display:block}
.nav{left:78px;top:126px;width:683px;height:30px;background:var(--nav);display:flex}
.nav a{font-size:10px;font-weight:700;color:var(--red);text-decoration:none;padding:0 15px;line-height:30px}
.nav a.active{background:var(--red);color:#fff}
/* hero */
.hero{left:78px;top:160px;width:683px;height:280px;background:linear-gradient(135deg,#8b98a4,#cfd3d2 45%,#b6a58c)}
.hero-caption{left:0;top:237px;width:683px;height:34px;background:rgba(20,20,20,.72);color:#fff;font-size:16px;font-weight:700;text-align:center;line-height:34px}
.arrow{top:127px;width:20px;height:26px;background:rgba(0,0,0,.55)}
.feedback{right:0;top:257px;width:22px;height:96px;background:var(--red);color:#fff;font-size:8px;font-weight:700;writing-mode:vertical-rl;text-align:center;line-height:22px}
/* sections */
h2{font-size:11px;font-weight:700;color:var(--ink);text-transform:uppercase;line-height:1.3}
h2 em{font-style:normal;color:var(--red)}
p{font-size:8.5px}
.btn{background:var(--red);color:#fff;font-size:8px;font-weight:700;width:60px;height:20px;line-height:20px;text-align:center;border-radius:2px}
.photo{background:linear-gradient(135deg,#b9b1a2,#e2ddd2)}
.rule{height:1px;background:var(--line)}
.quote-mark{width:40px;height:82px;background:var(--red);color:#fff;font-size:30px;font-weight:700;text-align:center;line-height:50px}
.client h3{font-size:9px;font-weight:700;color:var(--ink);margin-bottom:3px}
.client p{font-size:7.5px}
.client small{display:block;font-size:6.5px;font-weight:700;color:var(--ink);margin-top:4px}
.shares{display:flex;gap:4px;margin-top:5px}
.shares span{width:24px;height:10px;background:#ddd;border-radius:2px}
.nav-dots{display:flex;gap:3px}
.nav-dots span{width:12px;height:12px;background:var(--red);border-radius:50%}
/* footer */
.footer-links{left:78px;top:1124px;display:flex;gap:12px;font-size:7.5px;color:var(--text)}
.copyright{left:78px;top:1156px;font-size:7px;color:var(--muted)}
.partner{left:680px;top:1116px;display:flex;align-items:center;gap:5px}
.partner i{width:14px;height:14px;background:var(--navy);display:block}
.partner span{font-size:8px;font-weight:700;color:var(--navy);width:70px;line-height:1.1}
.social{left:700px;top:1152px;display:flex;gap:3px}
.social span{width:10px;height:10px;background:var(--navy);border-radius:2px}
</style>
</head>
<body>

<header>
  <div class="abs brand"><span class="brand-mark"></span><span class="brand-name">Brightmoor Dwelling Co</span></div>
  <div class="abs phone">1-800-555-0172</div>
  <div class="abs email">hello@brightmoordwelling.example</div>
  <div class="abs search">Search
    <svg width="9" height="9" viewBox="0 0 10 10"><circle cx="4" cy="4" r="3" fill="none" stroke="#888" stroke-width="1.3"/><line x1="6.3" y1="6.3" x2="9" y2="9" stroke="#888" stroke-width="1.3"/></svg>
  </div>
  <div class="abs quote"><i></i>Request a Quote</div>
  <nav class="abs nav">
    <a class="active">HOME</a><a>SERVICES</a><a>FLOOR PLANS</a><a>GALLERY</a><a>VIDEOS</a><a>TESTIMONIALS</a><a>CONTACT US</a>
  </nav>
</header>

<section class="abs hero" role="img" aria-label="Furnished living room interior of a temporary home">
  <div class="abs arrow" style="left:0"><svg width="20" height="26"><path d="M12 7 6 13l6 6" fill="none" stroke="#fff" stroke-width="2"/></svg></div>
  <div class="abs arrow" style="right:0"><svg width="20" height="26"><path d="M8 7l6 6-6 6" fill="none" stroke="#fff" stroke-width="2"/></svg></div>
  <div class="abs hero-caption">Sed ut perspiciatis unde omnis iste natus error sit voluptatem</div>
</section>
<div class="abs feedback">FEEDBACK</div>

<section class="abs" style="left:78px;top:453px;width:500px">
  <h2>Welcome to <em>Brightmoor Dwelling Co</em> your onsite temporary housing experts</h2>
  <div class="rule" style="margin:5px 0 6px"></div>
  <p>We are the leading provider of On-Site Temporary Housing. We provide Mobile Homes, Park Models and Travel Trailers. These homes are brought to your client's home site and set up. Your client can stay right at home to oversee the reconstruction.</p>
  <p style="margin-top:8px">We have been in the On-Site Temporary Housing business for over 30 years. We have a courteous and experienced staff.</p>
</section>
<div class="abs btn" style="left:78px;top:573px">READ MORE</div>
<div class="abs photo" style="left:596px;top:453px;width:165px;height:151px" role="img" aria-label="Mobile home set up on a residential lot"></div>

<!-- service columns -->
<h2 class="abs" style="left:78px;top:630px">Commercial</h2>
<div class="abs photo" style="left:78px;top:655px;width:213px;height:80px" role="img" aria-label="Crew delivering a temporary housing unit"></div>
<p class="abs" style="left:78px;top:745px;width:213px">Sed ut perspiciatis unde omnis iste natus error sit voluptatem accusantium</p>
<div class="abs btn" style="left:78px;top:820px">READ MORE</div>

<h2 class="abs" style="left:313px;top:630px">Residential</h2>
<div class="abs photo" style="left:313px;top:655px;width:213px;height:80px" role="img" aria-label="Temporary home parked beside a house under remodel"></div>
<p class="abs" style="left:313px;top:745px;width:213px">Sed ut perspiciatis unde omnis iste natus error sit voluptatem accusantium</p>
<div class="abs btn" style="left:313px;top:820px">READ MORE</div>

<h2 class="abs" style="left:548px;top:630px">Past Projects</h2>
<div class="abs photo" style="left:548px;top:655px;width:213px;height:80px" role="img" aria-label="Completed home construction project"></div>
<p class="abs" style="left:548px;top:745px;width:213px">Sed ut perspiciatis unde omnis iste natus error sit voluptatem accusantium</p>
<div class="abs btn" style="left:548px;top:820px">READ MORE</div>

<!-- how it works -->
<h2 class="abs" style="left:78px;top:873px">How it works</h2>
<div class="abs photo" style="left:78px;top:898px;width:213px;height:100px" role="img" aria-label="Travel trailer on site"></div>
<p class="abs" style="left:78px;top:1020px;font-weight:700;color:var(--ink)">Summit Travel Trailer</p>
<div class="abs btn" style="left:78px;top:1062px">READ MORE</div>

<!-- testimonials -->
<h2 class="abs" style="left:313px;top:873px">Testimonials</h2>
<div class="abs nav-dots" style="left:498px;top:873px"><span></span><span></span></div>
<div class="abs quote-mark" style="left:313px;top:900px">“</div>
<div class="abs client" style="left:361px;top:900px;width:165px">
  <h3>CLIENT NAME</h3>
  <p>Sed ut perspiciatis unde omnis iste natus error sit voluptatem accusantium doloremque laudantium.</p>
  <p style="margin-top:3px">Ipsum et facilisis, tincidunt vitae dolor sed nulla.</p>
  <small>WWW.CLIENTREVIEW.EXAMPLE</small>
  <div class="shares"><span></span><span></span><span></span></div>
</div>
<div class="abs btn" style="left:313px;top:1048px">READ MORE</div>

<!-- gallery -->
<h2 class="abs" style="left:548px;top:873px">Gallery</h2>
<div class="abs photo" style="left:548px;top:898px;width:213px;height:66px" role="img" aria-label="Kitchen inside a rental unit"></div>
<div class="abs photo" style="left:548px;top:970px;width:68px;height:62px" role="img" aria-label="Exterior of a park model"></div>
<div class="abs photo" style="left:620px;top:970px;width:69px;height:62px" role="img" aria-label="Bedroom interior"></div>
<div class="abs photo" style="left:693px;top:970px;width:68px;height:62px" role="img" aria-label="Living area interior"></div>
<div class="abs btn" style="left:548px;top:1058px">READ MORE</div>

<footer>
  <div class="abs rule" style="left:78px;top:1110px;width:683px"></div>
  <div class="abs footer-links"><span>Home</span><span>Services</span><span>Floor Plans</span><span>Gallery</span><span>Videos</span><span>Testimonials</span><span>Contact US</span></div>
  <div class="abs rule" style="left:78px;top:1144px;width:580px"></div>
  <div class="abs copyright">© BRIGHTMOORDWELLING 2013 . All Rights Reserved</div>
  <div class="abs partner"><i></i><span>Cobalt Portable Lodging</span></div>
  <div class="abs social"><span></span><span></span><span></span><span></span></div>
</footer>

</body>
</html>
```